Coming Soon page for a new fitness startup

We are a new startup based in Toronto, Canada working on a site and mobile app where people can register for athletic events such as running, cycling, triathlon, SUP, etc.

Participants will also be able to manage their clubs and team, and connect their fitness trackers so they have all their fitness data and friends in one place.

I like very simple designs and lots of whitespace. So no need for icons or unnecessary graphics.

I prefer having a mobile phone app instead of a hero image. No need to worry about the details within the mobile app for now, we can fill it in later. Here are some landing pages that I like.
https://pixelshelf.example/tormundlaksa/buckets/493817-Landing-Page

Attached is a wireframe that gives some sample content for each of the sections. Please do not take the wireframe too literally, it is only meant to illustrate the content that we are experimenting with and should give an idea of how much text will be on the page.

I have also attached the company logo files. The logo is not being used yet so feel free to simplify the logo if it doesn't look great with your design. For example, I'm ok with just the name "vexqari" in white if that looks better.

Target Market(s)

Ages 25 to 45. Interested in running, cycling, triathlon, SUP, etc.

Industry/Entity Type

Fitness

Coding

Coded - Design and coding required

Number of Pages Required

1 page

Requirements
Should not have
• Any photos should not contain track and field events, or people in a gym. Any photos should have people running or cycling outdoors. I know that photos can be easily swapped out but it is distracting to review a design that has the wrong photos.

```html
<!DOCTYPE html>
<html lang="en">
<head>
<meta charset="utf-8">
<title>vexqari — Coming Soon</title>
<link rel="stylesheet" href="https://fonts.googleapis.com/css2?family=Lexend:wght@500&family=Montserrat:wght@400;500&family=Open+Sans:wght@400;600&display=swap">
<style>
  :root {
    --red: #d8232a;
    --red-deep: #c0171d;
    --red-text: #c4161c;
    --ink: #2b2b2b;
    --grey-text: #555;
    --dark: #3b3b3b;
    --footer: #3e3e3e;
    --white: #fff;
    --pink: #f6c5c7;
  }
  * { box-sizing: border-box; margin: 0; padding: 0; }
  html, body { width: 826px; height: 1200px; overflow: hidden; background: var(--white); }
  body { position: relative; font-family: "Open Sans", sans-serif; color: var(--ink); }
  .abs { position: absolute; }

  /* Hero */
  .hero { left: 0; top: 0; width: 826px; height: 470px; overflow: hidden; }
  .hero-photo { position: absolute; inset: 0;
    background: radial-gradient(ellipse at 70% 35%, #e8555a 0%, #d8232a 45%, #b8151b 100%); }
  .hero-curve { position: absolute; left: 0; bottom: 0; }
  .brand { left: 80px; top: 14px; display: flex; align-items: center; gap: 10px; }
  .brand-dot { width: 44px; height: 44px; border: 3px solid var(--white); border-radius: 50%; }
  .brand-name { font-family: "Montserrat", sans-serif; font-weight: 500; font-size: 34px; color: var(--white); letter-spacing: .5px; }
  .launch { left: 605px; top: 33px; font-size: 13px; font-weight: 600; color: var(--white); }

  .phone { left: 130px; top: 112px; width: 160px; height: 337px; background: var(--white);
    border: 1.5px solid #777; border-radius: 24px; }
  .phone-cam { left: 58px; top: 14px; width: 5px; height: 5px; border: 1px solid #555; border-radius: 50%; }
  .phone-speaker { left: 75px; top: 15px; width: 16px; height: 3px; border: 1px solid #555; border-radius: 2px; }
  .phone-screen { left: 6px; top: 37px; width: 146px; height: 258px;
    background: linear-gradient(170deg, #b8b8b0 0%, #9a8f6c 45%, #6b6a55 100%);
    display: flex; flex-direction: column; align-items: center; justify-content: center; gap: 8px; }
  .phone-screen .brand-dot { width: 30px; height: 30px; border-width: 2.5px; }
  .phone-screen .brand-name { font-size: 26px; }
  .phone-home { left: 64px; top: 303px; width: 28px; height: 28px; border: 1.5px solid #444; border-radius: 50%; }

  .hero-title { left: 347px; top: 137px; width: 400px; font-family: "Lexend", sans-serif; font-weight: 500;
    font-size: 26px; line-height: 27px; color: var(--white); }
  .hero-lede { left: 347px; top: 203px; width: 360px; font-size: 11.5px; line-height: 15px; color: var(--pink); }
  .hero-invite { left: 350px; top: 254px; width: 320px; font-family: "Montserrat", sans-serif; font-size: 12px; line-height: 16px; color: var(--white); }
  .signup { left: 343px; top: 298px; width: 351px; height: 40px; border-radius: 20px; background: rgba(255,255,255,.35); }
  .signup-field { position: absolute; left: 4px; top: 4px; width: 342px; height: 31px; border-radius: 16px; background: var(--white);
    display: flex; align-items: center; padding-left: 15px; gap: 10px; font-size: 11px; color: #555; }
  .signup-btn { position: absolute; right: 8px; top: 7px; width: 83px; height: 25px; border-radius: 13px; background: #4a4a4a;
    color: var(--white); font-size: 10px; font-weight: 600; display: flex; align-items: center; justify-content: center; }

  /* Features */
  .features-title { left: 0; width: 826px; top: 485px; text-align: center; font-family: "Montserrat", sans-serif; font-size: 23px; color: var(--red-text); letter-spacing: .5px; }
  .features-sub { left: 0; width: 826px; top: 518px; text-align: center; font-family: "Montserrat", sans-serif; font-size: 15.5px; color: var(--ink); }
  .card { top: 608px; width: 211px; height: 186px; background: var(--white); box-shadow: 0 1px 5px rgba(0,0,0,.16); text-align: center; }
  .card-badge { position: absolute; left: 58px; top: -40px; }
  .card-title { position: absolute; left: 0; right: 0; top: 66px; font-family: "Montserrat", sans-serif; font-size: 15px; color: #333; }
  .card-text { position: absolute; left: 14px; right: 14px; top: 96px; font-size: 7.8px; line-height: 14px; color: var(--grey-text); }

  /* Organizer */
  .organize { left: 0; top: 837px; width: 826px; height: 310px; }
  .organize-photo { position: absolute; inset: 0; background: linear-gradient(100deg, #474747 0%, #3a3a3a 50%, #333 100%); }
  .notch { position: absolute; left: 0; top: -1px; }
  .notch-dot { left: 391px; top: 820px; width: 28px; height: 28px; border: 2px solid #555; border-radius: 50%; background: var(--white); }
  .org-title { left: 83px; top: 890px; font-family: "Montserrat", sans-serif; font-size: 23px; color: var(--white); letter-spacing: .5px; }
  .org-sub { left: 84px; top: 929px; font-family: "Montserrat", sans-serif; font-size: 14px; color: var(--white); }
  .org-text { left: 84px; top: 963px; width: 270px; font-size: 10.5px; line-height: 15.6px; color: #eee; }
  .org-link { left: 84px; top: 1038px; font-size: 10.5px; color: var(--white); }
  .contact-title { left: 410px; top: 886px; font-family: "Montserrat", sans-serif; font-size: 14px; font-weight: 500; color: var(--white); }
  .field { left: 409px; width: 314px; border: 1px solid #bbb; font-size: 10px; color: var(--white); padding: 8px 12px; }
  .send { left: 638px; top: 1075px; width: 88px; height: 28px; background: var(--red); color: var(--white);
    font-size: 11px; display: flex; align-items: center; justify-content: center; letter-spacing: .5px; }

  /* Footer */
  .footer { left: 0; top: 1147px; width: 826px; height: 53px; background: var(--footer); color: #ddd; font-size: 10.5px; }
  .footer-links { position: absolute; left: 87px; top: 17px; }
  .footer-links span { margin: 0 8px; }
  .social { position: absolute; left: 406px; top: 16px; display: flex; gap: 17px; }
  .social i { display: block; width: 15px; height: 15px; border-radius: 50%; background: #ddd; }
  .copyright { position: absolute; left: 557px; top: 18px; font-size: 10px; }
</style>
</head>
<body>

<header class="abs hero">
  <div class="hero-photo" role="img" aria-label="Red-tinted photo of a smiling cyclist riding outdoors"></div>
  <svg class="hero-curve" width="826" height="60" viewBox="0 0 826 60" aria-hidden="true">
    <path d="M0 60 Q413 -50 826 60 Z" fill="#fff"/>
  </svg>
</header>

<div class="abs brand">
  <span class="brand-dot"></span><span class="brand-name">vexqari</span>
</div>
<p class="abs launch">Launching Spring 2018</p>

<div class="abs phone">
  <span class="abs phone-cam"></span>
  <span class="abs phone-speaker"></span>
  <div class="abs phone-screen" role="img" aria-label="App splash screen with a photo of runners outdoors">
    <span class="brand-dot"></span><span class="brand-name">vexqari</span>
  </div>
  <span class="abs phone-home"></span>
</div>

<h1 class="abs hero-title">Connect Your Training, Friends and Events in One Place</h1>
<p class="abs hero-lede">Amagnis dis parturient montes nascetur ridiculus mus In iaculis facilisis massa Etiam eu urna Sed porta Suspendisse</p>
<p class="abs hero-invite">Join Our Email list. A referral program is coming and you'll want to be the first to know</p>
<form class="abs signup">
  <div class="signup-field">
    <svg width="15" height="11" viewBox="0 0 15 11" aria-hidden="true"><rect width="15" height="11" rx="1" fill="#777"/><path d="M1 1 L7.5 6 L14 1" stroke="#fff" stroke-width="1.2" fill="none"/></svg>
    Email address
  </div>
  <span class="signup-btn">Notify Me</span>
</form>

<h2 class="abs features-title">Training and Racing all in one Place</h2>
<p class="abs features-sub">A New Fitness Community is Coming Soon</p>

<section class="abs card" style="left:84px">
  <svg class="card-badge" width="95" height="95" viewBox="0 0 95 95" aria-hidden="true">
    <circle cx="47.5" cy="47.5" r="45" fill="#fff"/>
    <path d="M12 72 A45 45 0 1 1 83 72" stroke="#555" stroke-width="4" fill="none"/>
    <g stroke="#c4161c" stroke-width="1.8" fill="none">
      <ellipse cx="38" cy="38" rx="8" ry="10"/><ellipse cx="57" cy="38" rx="8" ry="10"/><ellipse cx="47.5" cy="33" rx="8" ry="10"/>
      <path d="M38 48 L40 70 M57 48 L55 70 M47.5 43 L47.5 70"/>
    </g>
  </svg>
  <h3 class="card-title">Find Event</h3>
  <p class="card-text">Etiam eu urna Sed porta Suspendisse quam leo molestie sed luctus quis feugiat in pede Fusce tellus Sed metus augue convallis et vehicula ut pulvinar eu ante Integer orci</p>
</section>

<section class="abs card" style="left:308px">
  <svg class="card-badge" width="95" height="95" viewBox="0 0 95 95" aria-hidden="true">
    <circle cx="47.5" cy="47.5" r="45" fill="#fff"/>
    <path d="M12 72 A45 45 0 1 1 83 72" stroke="#555" stroke-width="4" fill="none"/>
    <g stroke="#c4161c" stroke-width="1.8" fill="none">
      <circle cx="47.5" cy="36" r="7"/><path d="M33 62 Q33 47 47.5 47 Q62 47 62 62 Z"/>
      <circle cx="32" cy="41" r="5"/><path d="M22 60 Q22 50 31 50"/>
      <circle cx="63" cy="41" r="5"/><path d="M73 60 Q73 50 64 50"/>
    </g>
  </svg>
  <h3 class="card-title">Invite Your Friends</h3>
  <p class="card-text">Etiam eu urna Sed porta Suspendisse quam leo molestie sed luctus quis feugiat in pede Fusce tellus Sed metus augue convallis et vehicula ut pulvinar eu ante Integer orci</p>
</section>

<section class="abs card" style="left:533px">
  <svg class="card-badge" width="95" height="95" viewBox="0 0 95 95" aria-hidden="true">
    <circle cx="47.5" cy="47.5" r="45" fill="#fff"/>
    <path d="M12 72 A45 45 0 1 1 83 72" stroke="#555" stroke-width="4" fill="none"/>
    <circle cx="33" cy="55" r="10" fill="#c4161c"/><circle cx="62" cy="55" r="10" fill="#c4161c"/>
    <path d="M33 55 L42 40 L56 40 L62 55 M42 40 L48 55 L56 40 M40 36 L46 36 M54 36 L60 34" stroke="#fff" stroke-width="2" fill="none"/>
  </svg>
  <h3 class="card-title">Connect Your Workouts</h3>
  <p class="card-text">Etiam eu urna Sed porta Suspendisse quam leo molestie sed luctus quis feugiat in pede Fusce tellus Sed metus augue convallis et vehicula ut pulvinar eu ante Integer orci</p>
</section>

<section class="abs organize">
  <div class="organize-photo" role="img" aria-label="Darkened photo of people running together outdoors"></div>
  <svg class="notch" width="826" height="20" viewBox="0 0 826 20" aria-hidden="true">
    <path d="M370 0 Q390 0 400 10 Q405 16 413 16 Q421 16 426 10 Q436 0 456 0 Z" fill="#fff"/>
  </svg>
</section>
<span class="abs notch-dot"></span>

<h2 class="abs org-title">Organizing an Event?</h2>
<p class="abs org-sub">Attracting participants is hard</p>
<p class="abs org-text">With your e3vent listed on vexqari we'll not not only handle the registration and payment process, we've also made it our own personal mission to drive up participation numbers across all events</p>
<p class="abs org-link">Contact Us to Learn More</p>

<h3 class="abs contact-title">We'd love to her from you</h3>
<div class="abs field" style="top:918px;height:29px">Your Name</div>
<div class="abs field" style="top:955px;height:29px">Email address</div>
<div class="abs field" style="top:994px;height:73px">Message</div>
<span class="abs send">SEND</span>

<footer class="abs footer">
  <nav class="footer-links">About Us<span>|</span>Developers<span>|</span>Careers</nav>
  <div class="social"><i aria-label="Social link"></i><i aria-label="Social link"></i><i aria-label="Social link"></i></div>
  <p class="copyright">© 2018 Company Name &nbsp;All right reserved</p>
</footer>

</body>
</html>
```